Bold Catchy But Classy flyer announcing that we are NOW OPEN IN LAGOS

VM (Velvet Moor) INTIMATES is a premium intimate apparel retailer for male & female intimate apparel, loungewear and bath and body products.

We just opened a new shop outlet in LAGOS and I need a superb, Catchy but Classy flyer to get the message out there that we are NOW OPEN IN LAGOS.

It will be used both digitally and also printed in a magazine which has given the following parameters:

HEIGHT: 11 inches
WIDTH: 8.5 inches
RESOLUTION: minimum of 300DPI

I have attached our logo (just so you can get our colours and name lettering style), WE LOVE PURPLE BACKGROUNDS!
Also, number of pictures (raw and edited versions) which can be cropped and used in the flyer (CopyRight is mine and so can't be used for anyone else!).
However, where available, designer can use pictures & vectors that they have rights to utilise.

Social media handles to appear on the flyer:
Instagram & Twitter: @velvetmoor
Facebook: @VMIntimates

Email: admin@velvetmoorng-example.com
Tel: +2348107265190

Address:
VM INTIMATES
Plaza Corvette
27 Okonrinde Street
Off Babatunde Ilesanmi
Victoria Island
Lagos

Target Market(s)

MEN & WOMEN (20YRS-60YRS)

Industry/Entity Type

Lingerie

Font styles to use
Sans Serif

Colors
6b449b
ffffff

Requirements
Must have
• All contact details (address, telephone, email & social media handles).
• A bold NOW IN LAGOS on the flyer.
Nice to have
• I like Flyers that have a pigmented coloured backdrop (see sample in image IMG_0159 which has a green backdrop but I would prefer deep purple
Should not have
• Long form description for social media types. Only symbols, please.

```html
<!DOCTYPE html>
<html lang="en">
<head>
<meta charset="utf-8">
<title>VM Intimates – Now Open In Lagos</title>
<link rel="stylesheet" href="https://fonts.googleapis.com/css2?family=Montserrat:wght@800;900&family=Kaushan+Script&family=Graduate&family=Lato:wght@400;700&display=swap">
<style>
  :root {
    --purple-deep: #2f1266;
    --purple-mid: #4a1f8c;
    --purple-brand: #6b449b;
    --purple-bright: #7b45d6;
    --purple-light: #a27be8;
    --white: #ffffff;
    --grey-shadow: #b9b4c4;
    --page-bg: #ece8f2;
  }
  * { box-sizing: border-box; margin: 0; padding: 0; }
  html, body { width: 1200px; height: 1200px; overflow: hidden; }
  body { background: var(--page-bg); position: relative; }

  .flyer {
    position: absolute; left: 152px; top: 20px;
    width: 896px; height: 1160px; overflow: hidden;
    color: var(--white);
    background:
      radial-gradient(circle at 90% 28%, rgba(190,160,240,.45) 0 60px, transparent 64px),
      radial-gradient(circle at 6% 50%, rgba(170,140,230,.35) 0 70px, transparent 74px),
      radial-gradient(ellipse at 50% 45%, rgba(150,110,220,.55), transparent 55%),
      linear-gradient(180deg, var(--purple-deep) 0%, var(--purple-mid) 35%, #5b33a0 60%, #583a92 100%);
  }

  .brand {
    position: absolute; top: 80px; left: 0; width: 100%;
    display: flex; justify-content: center; align-items: center; gap: 14px;
    font-family: "Lato", sans-serif; font-weight: 700; font-size: 46px; letter-spacing: 2px;
  }
  .brand-mark { width: 22px; height: 22px; background: var(--white); }

  .tagline {
    position: absolute; top: 183px; left: 0; width: 100%; text-align: center;
    font-family: "Montserrat", sans-serif; font-weight: 800; font-size: 12px; letter-spacing: .4px;
  }
  .headline-small {
    position: absolute; top: 196px; left: 0; width: 100%; text-align: center;
    font-family: "Montserrat", sans-serif; font-weight: 900; font-size: 64px; line-height: 1;
    letter-spacing: 1px;
  }
  .model-photo {
    position: absolute; left: 300px; top: 395px; width: 410px; height: 580px;
    border-radius: 200px 200px 30px 30px;
    background: linear-gradient(160deg, #1a1018 0%, #6e4a3c 35%, #b88a94 60%, #3a2230 100%);
    opacity: .9;
  }
  .headline-script {
    position: absolute; top: 262px; left: 0; width: 100%; text-align: center;
    font-family: "Kaushan Script", cursive; font-size: 118px; line-height: 1.2;
    white-space: nowrap;
  }
  .city {
    position: absolute; left: 108px; top: 790px; width: 690px; height: 230px;
  }
  .city text { font-family: "Graduate", serif; }

  .footer {
    position: absolute; left: 0; top: 1068px; width: 100%; height: 80px;
    font-family: "Lato", sans-serif; font-size: 17px; line-height: 22px;
  }
  .address { position: absolute; left: 45px; top: 0; }
  .address-name { display: flex; align-items: center; gap: 4px; font-weight: 700; font-size: 19px; }
  .address-lines { padding-left: 22px; }
  .contact { position: absolute; left: 393px; top: 12px; }
  .contact-row, .social-row { display: flex; align-items: center; gap: 14px; margin-bottom: 6px; }
  .contact-row:first-child { font-weight: 700; }
  .social { position: absolute; left: 704px; top: 0; font-weight: 700; }
  .social-row { margin-bottom: 1px; gap: 16px; }
  .social-dot { width: 12px; height: 12px; border-radius: 50%; background: var(--white); }
  .icon { width: 22px; height: 20px; fill: var(--white); }
</style>
</head>
<body>
  <main class="flyer">
    <div class="brand"><span class="brand-mark"></span><span>VM INTIMATES</span></div>
    <p class="tagline">...Unleash Your Inner Confidence</p>
    <p class="headline-small">we are</p>

    <div class="model-photo" role="img" aria-label="Photo of a model in black lingerie and a floral satin robe, seated on the lettering"></div>

    <p class="headline-script">Now Open In</p>

    <svg class="city" viewBox="0 0 690 230" aria-label="Lagos">
      <defs>
        <linearGradient id="city-fill" x1="0" y1="0" x2="0" y2="1">
          <stop offset="0" stop-color="#8f5ee6"/>
          <stop offset=".5" stop-color="#7440cf"/>
          <stop offset=".52" stop-color="#6a36c2"/>
          <stop offset="1" stop-color="#8b5ae0"/>
        </linearGradient>
      </defs>
      <text x="14" y="214" textLength="668" lengthAdjust="spacingAndGlyphs" font-size="270"
            fill="var(--grey-shadow)" stroke="var(--grey-shadow)" stroke-width="10">LAGOS</text>
      <text x="6" y="206" textLength="668" lengthAdjust="spacingAndGlyphs" font-size="270"
            fill="url(#city-fill)" stroke="var(--white)" stroke-width="10" paint-order="stroke">LAGOS</text>
    </svg>

    <footer class="footer">
      <div class="address">
        <div class="address-name">
          <svg class="icon" viewBox="0 0 24 24" aria-hidden="true"><path d="M12 2a7 7 0 0 0-7 7c0 5 7 13 7 13s7-8 7-13a7 7 0 0 0-7-7zm0 9.5A2.5 2.5 0 1 1 12 6.5a2.5 2.5 0 0 1 0 5z"/></svg>
          VM INTIMATES
        </div>
        <div class="address-lines">Plaza Corvette 27 Okonrinde Street Off<br>Babatunde Ilesanmi Victoria Island Lagos</div>
      </div>
      <div class="contact">
        <div class="contact-row">
          <svg class="icon" viewBox="0 0 24 24" aria-hidden="true"><path d="M6.6 10.8a15 15 0 0 0 6.6 6.6l2.2-2.2a1 1 0 0 1 1-.25 11.4 11.4 0 0 0 3.6.57 1 1 0 0 1 1 1V20a1 1 0 0 1-1 1A17 17 0 0 1 3 4a1 1 0 0 1 1-1h3.5a1 1 0 0 1 1 1c0 1.25.2 2.45.57 3.57a1 1 0 0 1-.25 1z"/></svg>
          +2348107265190
        </div>
        <div class="contact-row">
          <svg class="icon" viewBox="0 0 24 24" aria-hidden="true"><path d="M3 5h18v14H3zm2 2v.5l7 5 7-5V7zm0 3v7h14v-7l-7 5z"/></svg>
          admin@velvetmoorng-example.com
        </div>
      </div>
      <div class="social">
        <div class="social-row"><span class="social-dot"></span>@VMIntimates</div>
        <div class="social-row"><span class="social-dot"></span>@velvetmoor</div>
        <div class="social-row"><span class="social-dot"></span>@velvetmoor</div>
      </div>
    </footer>
  </main>
</body>
</html>
```